Security Camera Sign

14” high x 11” wide Color: Blue, Yellow, Black and white

Make the sign vertical
Replace red with blue
WARNING: Black over yellow
These premises are protected by Closed Circuit Television: On white
Images are recorded for crime prevention and public safety. Unauthorized access, theft or vandalism will result in prosecution: On Blue

Target Market(s)

Outdoor commercial building

Industry/Entity Type

Security

Requirements
Nice to have
• I would like the sign stand out. If you need more colors? Thanks Ok

```html
<!DOCTYPE html>
<html lang="en">
<head>
<meta charset="utf-8">
<title>Security Camera Sign</title>
<link rel="stylesheet" href="https://fonts.googleapis.com/css2?family=Carlito:wght@700&display=swap">
<style>
  :root {
    --backdrop: #d2d3d5;
    --sign-blue: #1175bf;
    --warning-yellow: #f4ed31;
    --ink: #0a0a0a;
    --paper: #ffffff;
    --camera-dark: #5a5c60;
    --camera-light: #c9cacc;
  }
  * { box-sizing: border-box; margin: 0; padding: 0; }
  html, body {
    width: 1200px;
    height: 938px;
    overflow: hidden;
    background: var(--backdrop);
  }
  body {
    position: relative;
    font-family: "Carlito", "Calibri", sans-serif;
    font-weight: 700;
  }
  .sign {
    position: absolute;
    left: 262px;
    top: 36px;
    width: 676px;
    height: 860px;
    border: 2px solid var(--ink);
    border-radius: 32px;
    overflow: hidden;
    background: var(--paper);
    box-shadow: 0 14px 12px -8px rgba(0,0,0,0.35);
  }
  .sign-header {
    position: absolute;
    left: 0; top: 0;
    width: 100%;
    height: 140px;
    background: var(--sign-blue);
  }
  .warning-plate {
    position: absolute;
    left: 38px;
    top: 26px;
    width: 596px;
    height: 90px;
    background: var(--warning-yellow);
    border: 3px solid var(--ink);
    border-radius: 10px;
    display: flex;
    align-items: center;
    justify-content: center;
  }
  .warning-word {
    font-size: 96px;
    line-height: 1;
    color: var(--ink);
    letter-spacing: 1px;
    margin-top: 6px;
  }
  .sign-body {
    position: absolute;
    left: 0; top: 140px;
    width: 100%;
    height: 530px;
  }
  .camera-art {
    position: absolute;
    left: 176px;
    top: 24px;
    width: 320px;
    height: 200px;
  }
  .notice {
    position: absolute;
    left: 0;
    top: 248px;
    width: 100%;
    text-align: center;
    font-size: 48px;
    line-height: 44px;
    color: var(--ink);
  }
  .sign-footer {
    position: absolute;
    left: 0; bottom: 0;
    width: 100%;
    height: 188px;
    background: var(--sign-blue);
    padding: 22px 26px 0 26px;
  }
  .legal {
    color: var(--paper);
    font-size: 30px;
    line-height: 36px;
    text-align: justify;
    letter-spacing: 0.3px;
  }
</style>
</head>
<body>
  <main class="sign">
    <header class="sign-header">
      <div class="warning-plate"><span class="warning-word">WARNING</span></div>
    </header>
    <section class="sign-body">
      <svg class="camera-art" role="img" aria-label="Illustration of a wall-mounted security camera with blue lens" viewBox="0 0 320 200">
        <defs>
          <linearGradient id="cameraTone" x1="0" y1="0" x2="1" y2="0">
            <stop offset="0" stop-color="var(--camera-dark)"/>
            <stop offset="1" stop-color="var(--camera-light)"/>
          </linearGradient>
        </defs>
        <rect x="0" y="0" width="320" height="200" rx="8" fill="url(#cameraTone)"/>
      </svg>
      <p class="notice">THESE<br>PREMISES ARE<br>PROTECTED<br>BY CLOSED<br>CIRCUIT<br>TELEVISION</p>
    </section>
    <footer class="sign-footer">
      <p class="legal">IMAGES ARE RECORDED FOR CRIME PREVENTION AND PUBLIC SAFETY. UNAUTHORIZED ACCESS, THEFT OR VANDALISM WILL RESULT IN PROSECUTION</p>
    </footer>
  </main>
</body>
</html>
```